Design the Taste: Help Us Cook Up a Fresh Brochure for Our Wholesale Food Brand!

Overview:
We are looking for a fresh, eye-catching brochure design for our wholesale food company. The brochure can be up to 6 pages and should be visually appealing while clearly presenting our products and services.

Reference:
Please use the attached previous brochure as a guide for layout and style inspiration.

Content Requirements:
The brochure must highlight our key food groups:

Frozen Entrées
Pizzas
Frozen Meals and Party Size
Dry goods and Pasta
Gift Baskets
Delicacies and Sweets
Can do private label
Additional Highlights:

We deliver to our customers.
All products are fresh and locally made in Nashville, TN.

Design Goals:

Modern, appetizing, and professional design

Easy to read and navigate
Should NOT say Bruno's Tuscan Grocer and Trattoria but brand colors should resemble our parent company Brunos Tuscan Grocer and Trattoria
Strong visual focus on our products
Also mention we can brand with clients information
Incorporate brand colors and style from previous brochure

Phone: (615) 555-0172
https://brunossupplyandgoods.example/
use any pictures from this site: https://brunossupplyandgoods.example/

use circle logo for Bruno's Fine Tuscan Kitchen

Outstanding family dining and exquisite imported Italian delights.
Today, you’ll find our locally made dishes in markets, mini-marts, and corner stores across the city, making it easy for your clients to enjoy the taste of Bruno’s at home.

Alongside our prepared foods, we offer a curated selection of imported Italian goods, handcrafted gift baskets made in-house, and our signature marinara sauce, lovingly created from my Lulu’s treasured recipes.

Use only our pictures of pizza, pasta, dry pasta, marina sauce, canolis, frozen entrees, frozen dishes and meat dishes provided in breif and on website. Can also use pictures from our facebook and instra gram
https://www.facebook.com/brunossupply
https://www.instagram.com/brunos_supply/

Target Market(s)

Liquior stores, mini markets, gas stations and mini food places

Industry/Entity Type

Food

Font styles to use
Other font styles liked:
• Valadimir script and new times roman

Colors
59FF00
82FF00
B8FF75
E3FFCB
F4FFEA
EB3D1F
EC4F4E
F09395
F8D3D4
FCEDEE

Requirements
Must have
• Item sectiosn metnioned, logo, phone number and webaddress

```html
<!DOCTYPE html>
<html lang="en">
<head>
<meta charset="utf-8">
<title>Wholesale Italian Food Brochure</title>
<link href="https://fonts.googleapis.com/css2?family=Great+Vibes&family=Tinos:ital,wght@0,400;0,700;1,700&display=swap" rel="stylesheet">
<style>
:root{
  --green:#59d400;
  --green-bright:#82ff00;
  --green-soft:#b8ff75;
  --red:#eb3d1f;
  --red-soft:#ec4f4e;
  --pink:#f09395;
  --ink:#222;
  --paper:#ffffff;
  --bg:#e9e9e9;
  --script:"Great Vibes",cursive;
  --serif:"Tinos","Times New Roman",serif;
}
*{box-sizing:border-box;margin:0;padding:0}
html,body{width:1200px;height:1144px;overflow:hidden;background:var(--bg)}
body{position:relative;font-family:var(--serif);color:var(--ink)}
.spread{position:absolute;left:20px;width:1160px;height:543px;display:flex;background:var(--paper);box-shadow:0 2px 8px rgba(0,0,0,.18)}
.spread--outside{top:20px}
.spread--inside{top:581px}
.panel{position:relative;width:386.67px;height:543px;overflow:hidden;background:var(--paper)}
.abs{position:absolute}
.center{left:0;right:0;text-align:center}
.overlay{position:absolute;inset:0;width:100%;height:100%}
.photo{position:absolute}
.script{font-family:var(--script);font-weight:400;line-height:1}
.script--green{color:var(--green)}
.script--red{color:var(--red)}
.h-item{font-weight:700;font-size:12px;line-height:1.1}
.h-item--red{color:var(--red)}
.h-item--green{color:var(--green)}
.desc{font-size:7.5px;line-height:1.3;color:#333}
.bubble-text{font-size:7.5px;line-height:1.35;color:#333;text-align:center}
.bubble-name{color:var(--red);font-weight:700;font-size:7.5px}
.quote-mark{font-family:var(--serif);font-weight:700;color:var(--red);font-size:22px;line-height:1}
.footer-bar{position:absolute;left:0;right:0;bottom:0;height:31px;display:flex;align-items:center;justify-content:center;gap:14px;color:#fff;font-size:9px}
.footer-bar--green{background:var(--green)}
.footer-bar--red{background:var(--red)}
.footer-bar .sep{width:1px;height:12px;background:rgba(255,255,255,.8)}
.footer-bar span{display:flex;align-items:center;gap:4px}
.order-btn{position:absolute;left:50%;transform:translateX(-50%);top:415px;width:130px;height:24px;border-radius:12px;background:linear-gradient(#f26a4f,var(--red));border:2px solid #fff;box-shadow:0 0 0 1.5px var(--red);color:#fff;font-size:12px;letter-spacing:1px;text-align:center;line-height:20px}
.cover-title{font-weight:700;font-size:35px;line-height:1.08;text-shadow:0 0 2px #fff,0 0 2px #fff,1px 1px 3px rgba(0,0,0,.35)}
.cover-title .red{color:var(--red)}
.cover-title .green{color:var(--green)}
.offer-grid{position:absolute;left:14px;right:14px;top:168px;display:grid;grid-template-columns:repeat(3,1fr);row-gap:10px}
.offer{display:flex;flex-direction:column;align-items:center;text-align:center}
.offer-frame{width:104px;height:110px;border-radius:52px 52px 10px 10px;border:2px solid var(--green);display:flex;justify-content:center;padding-top:6px;background:#fff}
.offer-frame--red{border-color:var(--red)}
.offer-photo{width:90px;height:90px;border-radius:50%;border:3px solid var(--green)}
.offer-frame--red .offer-photo{border-color:var(--red)}
.offer-title{font-weight:700;font-size:11.5px;line-height:1.05;margin-top:4px}
.offer-title--green{color:var(--green)}
.offer-title--red{color:var(--red)}
.offer-title--dark{color:#222}
.offer-desc{font-size:7.5px;line-height:1.25;margin-top:2px;color:#333}
.feature-icon{position:absolute;left:50%;transform:translateX(-50%);width:24px;height:24px}
</style>
</head>
<body>

<!-- Outside spread -->
<section class="spread spread--outside">

  <!-- Success panel -->
  <article class="panel">
    <h2 class="abs center script script--green" style="top:18px;font-size:27px">Dedicated to Your Success</h2>
    <p class="abs center h-item h-item--red" style="top:50px">Installation &amp; Service</p>
    <p class="abs center desc" style="top:63px">We provide free custom shelving and install high-efficiency freezers.</p>
    <p class="abs center h-item h-item--red" style="top:76px">In-House Demos</p>
    <p class="abs center desc" style="top:89px">Available upon request for product sampling.</p>
    <h3 class="abs center script script--green" style="top:114px;font-size:32px">Testimonial</h3>

    <svg class="overlay" viewBox="0 0 387 543" aria-hidden="true">
      <path d="M108 154 Q94 154 94 170 V206 Q94 222 110 222 H118 V240 L132 222 H282 Q296 222 296 206 V170 Q296 154 282 154" fill="none" stroke="var(--green)" stroke-width="1.3"/>
      <path d="M108 250 Q94 250 94 266 V302 Q94 318 110 318 H118 V336 L132 318 H282 Q296 318 296 302 V266 Q296 250 282 250" fill="none" stroke="var(--green)" stroke-width="1.3"/>
    </svg>
    <span class="abs quote-mark" style="left:98px;top:140px">&ldquo;</span>
    <span class="abs quote-mark" style="left:278px;top:140px">&rdquo;</span>
    <div class="abs bubble-text" style="left:112px;width:166px;top:160px">Bruno’s is eaten 2/3 times a month in my house hold. I usually order take out so I can't really speak to the service or experience inside but the food is always incredible. The cannoli's are out of this world.<br><span class="bubble-name">Nora K</span></div>
    <span class="abs quote-mark" style="left:98px;top:236px">&ldquo;</span>
    <span class="abs quote-mark" style="left:278px;top:236px">&rdquo;</span>
    <div class="abs bubble-text" style="left:112px;width:166px;top:262px">Traveling through we stumbled across this gem. Hands down THE BEST Italian food we have ever had! The service was amazing and the inside was so authentic.<br><span class="bubble-name">Sam T</span></div>

    <div class="photo" role="img" aria-label="Photo of a smiling woman holding a plate of pasta on a sunny terrace with a stone building behind"
      style="left:0;top:330px;width:387px;height:213px;background:linear-gradient(160deg,#e9dcc0 0%,#cdb98e 40%,#7d8b55 70%,#6b5540 100%);clip-path:path('M0 70 Q190 0 387 18 V213 H0 Z')"></div>
    <svg class="overlay" viewBox="0 0 387 543" aria-hidden="true">
      <path d="M0 400 Q190 330 387 348" fill="none" stroke="var(--red)" stroke-width="7"/>
    </svg>
  </article>

  <!-- Get started panel -->
  <article class="panel">
    <div class="photo" role="img" aria-label="Photo of a colorful cliffside seaside village at dusk"
      style="left:0;top:0;width:387px;height:400px;background:linear-gradient(180deg,#2a3d63 0%,#3b5478 30%,#8a5a4a 55%,#d94b26 80%,#e8452a 100%);clip-path:path('M0 0 H387 V300 Q220 300 160 370 Q110 400 0 400 Z')"></div>
    <svg class="overlay" viewBox="0 0 387 543" aria-hidden="true">
      <path d="M387 300 Q220 300 160 370 Q110 400 0 400" fill="none" stroke="var(--green)" stroke-width="6"/>
    </svg>
    <h2 class="abs center script script--green" style="top:78px;font-size:42px;text-shadow:0 0 2px #fff,0 0 2px #fff">Get Started</h2>
    <p class="abs center" style="top:120px;font-size:30px;font-weight:700;color:var(--red);text-shadow:0 0 2px #fff,0 0 2px #fff">Today</p>
    <p class="abs center" style="top:166px;font-size:19px;font-weight:700;color:#fff;line-height:1.05;text-shadow:1px 1px 3px rgba(0,0,0,.5)">We can brand with<br>your information</p>
    <div class="order-btn">ORDER NOW</div>
    <p class="abs center" style="top:452px;font-size:9px;letter-spacing:.5px;line-height:1.3">Bring Fresh, Premium Italian Products<br>to Your Customers!</p>
    <div class="footer-bar footer-bar--green">
      <span><svg width="9" height="9" viewBox="0 0 24 24" fill="#fff" aria-hidden="true"><path d="M6.6 10.8a15.1 15.1 0 0 0 6.6 6.6l2.2-2.2c.3-.3.7-.4 1-.2 1.1.4 2.3.6 3.6.6.6 0 1 .4 1 1V20c0 .6-.4 1-1 1A17 17 0 0 1 3 4c0-.6.4-1 1-1h3.5c.6 0 1 .4 1 1 0 1.3.2 2.5.6 3.6.1.3 0 .7-.2 1z"/></svg>(615)-555-0148</span>
      <i class="sep"></i>
      <span><svg width="9" height="9" viewBox="0 0 24 24" fill="none" stroke="#fff" stroke-width="2" aria-hidden="true"><circle cx="12" cy="12" r="10"/><path d="M2 12h20M12 2a15 15 0 0 1 0 20M12 2a15 15 0 0 0 0 20"/></svg>brunositalianmarket.example</span>
    </div>
  </article>

  <!-- Cover panel -->
  <article class="panel">
    <div class="photo" role="img" aria-label="Photo of a table of Italian dishes beside a sunny harbor"
      style="inset:0;background:linear-gradient(180deg,#d8cfc4 0%,#c9b9a6 25%,#eaeeef 45%,#bcd3d6 65%,#8f6a44 85%,#6b4a2c 100%)"></div>
    <svg class="overlay" viewBox="0 0 387 543" aria-hidden="true">
      <path d="M0 0 H90 L40 40 H0 Z" fill="var(--green)"/>
      <path d="M290 0 H387 V40 Z" fill="var(--red)"/>
      <path d="M0 190 Q150 300 387 230 V260 Q150 320 0 220 Z" fill="var(--red)" opacity=".95"/>
      <path d="M0 220 Q150 320 387 260 V390 H0 Z" fill="#fff" opacity=".72"/>
      <path d="M0 470 Q200 500 387 440 V512 H0 Z" fill="var(--red)"/>
    </svg>
    <div class="photo" role="img" aria-label="Photo of a bowl of rotini pasta in tomato sauce"
      style="left:204px;top:70px;width:164px;height:164px;border-radius:50%;border:6px solid var(--red);box-shadow:0 0 0 2px #fff;background:radial-gradient(circle,#e58a2a 0%,#d06a1c 55%,#8a4c2a 100%)"></div>
    <div class="photo" role="img" aria-label="Photo of a white plate of spaghetti with meat sauce and basil"
      style="left:95px;top:386px;width:200px;height:88px;border-radius:50% 50% 45% 45%;background:radial-gradient(ellipse at 50% 40%,#c5451e 0%,#b43b1a 50%,#f3efe8 72%,#f3efe8 100%)"></div>
    <h1 class="abs center cover-title" style="top:228px"><span class="red">Wholesale,</span><br><span class="red">Fresh &amp; Locally</span><br><span class="green">Made Food</span></h1>
    <p class="abs center" style="top:345px;font-size:12px;font-weight:700">Delivered Right to Your Store</p>
    <p class="abs center" style="top:362px;font-size:7.5px;letter-spacing:2px">Made in Nashville</p>
    <div class="footer-bar footer-bar--red">
      <span><svg width="9" height="9" viewBox="0 0 24 24" fill="#fff" aria-hidden="true"><path d="M6.6 10.8a15.1 15.1 0 0 0 6.6 6.6l2.2-2.2c.3-.3.7-.4 1-.2 1.1.4 2.3.6 3.6.6.6 0 1 .4 1 1V20c0 .6-.4 1-1 1A17 17 0 0 1 3 4c0-.6.4-1 1-1h3.5c.6 0 1 .4 1 1 0 1.3.2 2.5.6 3.6.1.3 0 .7-.2 1z"/></svg>(615)-555-0148</span>
      <i class="sep"></i>
      <span><svg width="9" height="9" viewBox="0 0 24 24" fill="none" stroke="#fff" stroke-width="2" aria-hidden="true"><circle cx="12" cy="12" r="10"/><path d="M2 12h20M12 2a15 15 0 0 1 0 20M12 2a15 15 0 0 0 0 20"/></svg>brunositalianmarket.example</span>
    </div>
  </article>
</section>

<!-- Inside spread -->
<section class="spread spread--inside">

  <!-- Offer panel -->
  <article class="panel">
    <div class="photo" role="img" aria-label="Photo of pizzas and pasta dishes on a dark table"
      style="left:0;top:0;width:387px;height:110px;background:linear-gradient(90deg,#3a2a22 0%,#b5542a 30%,#3a2c24 55%,#c7662f 80%,#2f241e 100%);clip-path:path('M0 0 H387 V60 Q200 120 0 90 Z')"></div>
    <svg class="overlay" viewBox="0 0 387 543" aria-hidden="true">
      <path d="M0 90 Q200 120 387 60" fill="none" stroke="var(--green)" stroke-width="6"/>
    </svg>
    <h2 class="abs center script script--red" style="top:120px;font-size:32px">What We Offer</h2>
    <div class="offer-grid">
      <div class="offer">
        <div class="offer-frame"><div class="offer-photo" role="img" aria-label="Photo of a frozen pizza entrée" style="background:radial-gradient(circle,#e9c98a,#c9673a 70%)"></div></div>
        <p class="offer-title offer-title--green">Frozen Entrées</p>
        <p class="offer-desc">Homemade, fresh,<br>and specialty<br>imported entrées.</p>
      </div>
      <div class="offer">
        <div class="offer-frame offer-frame--red"><div class="offer-photo" role="img" aria-label="Photo of frozen pizzas wrapped in plastic" style="background:radial-gradient(circle,#f3e2dc,#d38a84 75%)"></div></div>
        <p class="offer-title offer-title--dark">Pizzas</p>
        <p class="offer-desc">Freshly made pizzas with<br>specialty and<br>gluten-free options.</p>
      </div>
      <div class="offer">
        <div class="offer-frame offer-frame--red"><div class="offer-photo" role="img" aria-label="Photo of a freezer stocked with party size meals" style="background:radial-gradient(circle,#cfe3ea,#6f99ad 75%)"></div></div>
        <p class="offer-title offer-title--red">Frozen Meals &amp;<br>Party Sizes</p>
        <p class="offer-desc">Perfect for catering or<br>large parties.</p>
      </div>
      <div class="offer">
        <div class="offer-frame"><div class="offer-photo" role="img" aria-label="Photo of a skillet of pasta" style="background:radial-gradient(circle,#d99a3a,#7a4a24 75%)"></div></div>
        <p class="offer-title offer-title--green">Bruno’s Brand<br>Pasta</p>
        <p class="offer-desc">Handmade, authentic<br>pasta from Italy.</p>
      </div>
      <div class="offer">
        <div class="offer-frame offer-frame--red"><div class="offer-photo" role="img" aria-label="Photo of a gift basket of Italian goods" style="background:radial-gradient(circle,#c64a3a,#6b3a2a 75%)"></div></div>
        <p class="offer-title offer-title--dark">Gift Baskets</p>
        <p class="offer-desc">Curated baskets with<br>premium Italian goods.</p>
      </div>
      <div class="offer">
        <div class="offer-frame offer-frame--red"><div class="offer-photo" role="img" aria-label="Photo of a sliced cured meat roast" style="background:radial-gradient(circle,#c9705a,#7a3024 75%)"></div></div>
        <p class="offer-title offer-title--red">Delicacies &amp;<br>Sweets</p>
        <p class="offer-desc">Delicacies &amp; Sweets</p>
      </div>
    </div>
  </article>

  <!-- Delivery panel -->
  <article class="panel">
    <h2 class="abs center script script--green" style="top:18px;font-size:27px">Fresh, Fast Delivery</h2>
    <svg class="feature-icon" style="top:60px" viewBox="0 0 24 24" fill="none" stroke="#555" stroke-width="1.4" aria-hidden="true"><circle cx="12" cy="12" r="11"/><path d="M6 14h9v-5H6zM15 11h2l1.5 3H15M8 16.5a1 1 0 1 0 0 .1M16 16.5a1 1 0 1 0 0 .1"/></svg>
    <p class="abs center h-item h-item--red" style="top:87px">We Deliver Locally</p>
    <p class="abs center desc" style="top:100px">Serving liquor stores, mini-markets, gas stations, and small food shops.</p>
    <svg class="feature-icon" style="top:116px" viewBox="0 0 24 24" fill="none" stroke="#555" stroke-width="1.4" aria-hidden="true"><circle cx="12" cy="12" r="11"/><circle cx="12" cy="12" r="7"/><path d="M9 12l2 2 4-4"/></svg>
    <p class="abs center h-item h-item--red" style="top:145px">Always Fresh</p>
    <p class="abs center desc" style="top:158px">Made fresh and locally in Nashville, TN.</p>
    <svg class="feature-icon" style="top:174px" viewBox="0 0 24 24" fill="none" stroke="#555" stroke-width="1.4" aria-hidden="true"><circle cx="12" cy="12" r="11"/><path d="M12 5l1.6 1.6 2.2-.4.4 2.2L18 10l-1 2 1 2-1.8 1.6-.4 2.2-2.2-.4L12 19l-1.6-1.6-2.2.4-.4-2.2L6 14l1-2-1-2 1.8-1.6.4-2.2 2.2.4z"/></svg>
    <p class="abs center h-item h-item--red" style="top:203px">Custom Branding</p>
    <p class="abs center desc" style="top:216px">Let us brand our products with your logo or store's name to boost your marketing.</p>
    <div class="photo" role="img" aria-label="Photo of pizzas, pasta nests, olives and tomatoes on a dark table"
      style="left:0;top:240px;width:387px;height:303px;background:linear-gradient(135deg,#3b2a22 0%,#b94a28 25%,#2e241f 45%,#d07a3a 65%,#2a201b 85%,#a8402a 100%);clip-path:path('M0 20 Q200 -10 387 30 V303 H0 Z')"></div>
    <svg class="overlay" viewBox="0 0 387 543" aria-hidden="true">
      <path d="M0 260 Q200 230 387 270" fill="none" stroke="var(--red)" stroke-width="7"/>
    </svg>
  </article>

  <!-- Story panel -->
  <article class="panel">
    <div class="photo" role="img" aria-label="Photo of a smiling couple outdoors in a sunny city"
      style="left:0;top:0;width:387px;height:200px;background:linear-gradient(120deg,#9a9088 0%,#d8c7b3 35%,#c9b8a4 60%,#e8e2da 100%);clip-path:path('M0 0 H387 V140 Q220 210 0 170 Z')"></div>
    <svg class="overlay" viewBox="0 0 387 543" aria-hidden="true">
      <path d="M0 170 Q220 210 387 140" fill="none" stroke="var(--green)" stroke-width="7"/>
    </svg>
    <h2 class="abs center script script--green" style="top:208px;font-size:30px">Our Story</h2>
    <p class="abs center h-item h-item--red" style="top:250px">Family Tradition</p>
    <p class="abs center desc" style="top:263px">Our recipes date back to 1964, passed down through four generations.</p>
    <p class="abs center h-item h-item--red" style="top:276px">Quality Commitment</p>
    <p class="abs center desc" style="top:289px">We use only the finest, locally sourced ingredients.</p>
    <h2 class="abs center script script--red" style="top:316px;font-size:32px">Why Choose Us?</h2>
    <p class="abs center h-item h-item--green" style="top:358px">Guaranteed Buyback</p>
    <p class="abs center desc" style="top:371px">No risk — we offer a buyback guarantee on unsold products.</p>
    <p class="abs center h-item h-item--green" style="top:384px">Weekly Restock</p>
    <p class="abs center desc" style="top:397px">Reliable, timely deliveries directly to your store.</p>
    <div class="photo" role="img" aria-label="Photo of a white plate of spaghetti with tomato sauce and basil"
      style="left:40px;top:430px;width:320px;height:140px;border-radius:50%;background:radial-gradient(ellipse at 50% 35%,#d9822e 0%,#c9501f 38%,#f4f1ec 60%,#e8e4de 100%)"></div>
  </article>
</section>

</body>
</html>
```